Orvik Lines website

i'm looking for a promotional website for my business.
we provide Rope Access, Work at Height & Difficult Access services.
we treat water leak into buildings, external renovation of buildings, windows cleaning, confined spaces services and practically jobs in which the access is difficult.
here are examples of web site i like :
http://www.layoutbazaar.example/wordpress-themes/51872.html
http://www.layoutbazaar.example/joomla-templates/51294.html

private people, commercial household chiefs, maintenance managers

Business

• - mobile friendly
- frindlo redirection
- 5 tabs
- one more customizable page - so i can add a photo and a description of the service corresponding (for now i offer 7 different services)
- contact us on each page with no redirection
- we are offering 7 different services
the website will be published in Israel which means right to left or centered for english option in the future. (logo on left hand corner)

- no flash
- should be future customisable - for future
• - a space for a slogan
- non scrollable
- photos on the landing page + redirection to gallery (photos and short films)
- 3 dynamic banners with short description of the theme of each, clicking on the banner after it opened will redirect to it's corresponding page.

```html
<!DOCTYPE html>
<html lang="en">
<head>
<meta charset="utf-8">
<title>Orvik Lines</title>
<link rel="stylesheet" href="https://fonts.googleapis.com/css2?family=PT+Sans+Narrow:wght@400;700&family=PT+Sans:wght@400;700&display=swap">
<style>
  :root {
    --page-bg: #bfc2c6;
    --ink: #2b2d30;
    --ink-soft: #3c3f43;
    --black: #0b0b0c;
    --white: #ffffff;
    --rule: #6f7276;
    --button-bg: #e4e5e6;
    --footer-top: #6a6c70;
    --footer-bottom: #4f5154;
    --footer-text: #e6e7e8;
    --hero-top: #c9ccd2;
    --hero-mid: #5a78c4;
    --hero-deep: #2f4a8e;
    --caption-bg: rgba(40, 42, 46, 0.62);
  }
  * { box-sizing: border-box; margin: 0; padding: 0; }
  html, body { width: 945px; height: 1200px; overflow: hidden; }
  body {
    position: relative;
    background: radial-gradient(ellipse at 50% 40%, #c8cacd 0%, var(--page-bg) 60%, #b3b6ba 100%);
    font-family: "PT Sans", Arial, sans-serif;
    color: var(--ink);
  }
  .abs { position: absolute; }
  .narrow { font-family: "PT Sans Narrow", "Arial Narrow", sans-serif; }

  /* header */
  .brand { left: 128px; top: 44px; display: flex; align-items: center; gap: 10px; }
  .brand-mark { width: 40px; height: 40px; border-radius: 50%; background: var(--black); }
  .brand-name { font-family: "PT Sans Narrow", sans-serif; font-weight: 700; font-size: 34px; color: var(--black); letter-spacing: .5px; }
  .lang { top: 37px; display: flex; align-items: center; gap: 4px; font-size: 8.5px; color: var(--ink); }
  .flag { width: 23px; height: 14px; display: block; }
  .nav { left: 0; top: 100px; width: 945px; height: 46px; }
  .nav-tab { left: 465px; top: 0; width: 65px; height: 46px; background: var(--black); border-radius: 3px 3px 0 0; }
  .nav a { position: absolute; top: 25px; font-family: "PT Sans Narrow", sans-serif; font-size: 13px; color: var(--black); text-decoration: none; }
  .nav a.active { color: var(--white); }

  /* hero */
  .bar { left: 0; width: 945px; height: 8px; background: var(--black); }
  .hero { left: 0; top: 154px; width: 945px; height: 383px;
    background: linear-gradient(160deg, var(--hero-top) 0%, #a9b0bd 25%, var(--hero-mid) 55%, var(--hero-deep) 80%, #8fa0c6 100%); }
  .caption { left: 0; top: 322px; width: 340px; height: 135px; background: var(--caption-bg); padding: 9px 16px 0 22px; color: var(--white); }
  .caption h1 { font-family: "PT Sans Narrow", sans-serif; font-weight: 700; font-size: 20px; letter-spacing: .2px; padding-bottom: 3px; border-bottom: 1px solid rgba(255,255,255,.75); width: 302px; text-shadow: 0 1px 2px rgba(0,0,0,.6); }
  .caption p { font-size: 9.6px; line-height: 16.5px; margin-top: 7px; color: #e3e4e6; }
  .arrow { top: 457px; width: 33px; height: 32px; background: rgba(235,236,238,.9); }
  .arrow svg { width: 33px; height: 32px; display: block; }

  /* services */
  .section-title { font-family: "PT Sans Narrow", sans-serif; font-size: 21px; color: var(--ink-soft); }
  .service { top: 606px; width: 160px; }
  .service-photo { width: 132px; height: 132px; border-radius: 50%; border: 3px solid var(--black); }
  .service-name { position: absolute; font-family: "PT Sans Narrow", sans-serif; font-size: 14.5px; line-height: 16.5px; color: var(--ink-soft); }

  /* welcome + news */
  .block-title { font-family: "PT Sans Narrow", sans-serif; font-size: 17px; color: var(--ink); padding-bottom: 2px; border-bottom: 1px solid var(--rule); }
  .welcome { left: 103px; top: 838px; width: 459px; }
  .welcome .lead { font-size: 10.4px; margin-top: 6px; color: var(--ink); }
  .welcome .body { font-size: 8.1px; line-height: 14px; margin-top: 7px; text-align: justify; color: var(--ink-soft); }
  .btn { background: var(--button-bg); font-family: "PT Sans Narrow", sans-serif; font-size: 12px; color: var(--black); text-align: center; line-height: 26px; height: 26px; }
  .news { left: 605px; top: 837px; width: 233px; }
  .news-item { position: absolute; left: 603px; width: 236px; }
  .news-date { position: absolute; left: 0; top: 0; width: 54px; height: 54px; border-radius: 50%; background: var(--black); color: var(--white); font-size: 10px; text-align: center; line-height: 54px; }
  .news-text { position: absolute; left: 60px; top: 8px; width: 176px; font-size: 8.1px; line-height: 11px; text-align: justify; color: var(--ink-soft); }

  /* footer */
  .footer { left: 0; top: 1056px; width: 945px; height: 144px; background: linear-gradient(180deg, var(--footer-top), var(--footer-bottom)); color: var(--footer-text); }
  .footer h3 { position: absolute; left: 108px; top: 22px; font-family: "PT Sans Narrow", sans-serif; font-weight: 700; font-size: 15.5px; color: #f1f1f2; }
  .email { position: absolute; left: 108px; top: 57px; width: 204px; height: 25px; background: var(--white); border: 1px solid #cfd0d2; border-radius: 2px; font-size: 8px; font-style: italic; color: #8a8c90; padding: 7px 0 0 12px; }
  .subscribe { position: absolute; left: 229px; top: 91px; width: 82px; height: 25px; background: #1a1a1b; color: var(--white); font-family: "PT Sans Narrow", sans-serif; font-weight: 700; font-size: 12px; text-align: center; line-height: 25px; }
  .social { position: absolute; top: 34px; width: 21px; height: 21px; border-radius: 2px; }
  .links { position: absolute; right: 104px; top: 67px; font-size: 8.3px; color: var(--footer-text); }
  .links span { margin: 0 4px; }
  .copyright { position: absolute; right: 106px; top: 89px; font-size: 8.3px; color: var(--footer-text); }
</style>
</head>
<body>

<header>
  <div class="abs brand"><span class="brand-mark"></span><span class="brand-name">Orvik Lines</span></div>

  <div class="abs lang" style="left:680px;">
    <svg class="flag" viewBox="0 0 23 14" role="img" aria-label="Israel language flag"><rect width="23" height="14" fill="#fff" stroke="#c9c9c9" stroke-width=".5"/><rect y="2" width="23" height="2" fill="#1d4fb0"/><rect y="10" width="23" height="2" fill="#1d4fb0"/></svg>
    <span>Israel</span>
  </div>
  <div class="abs lang" style="left:760px;">
    <svg class="flag" viewBox="0 0 23 14" role="img" aria-label="English language flag"><rect width="23" height="14" fill="#1f3a8a"/><rect x="9" width="5" height="14" fill="#fff"/><rect y="4.5" width="23" height="5" fill="#fff"/><rect x="10" width="3" height="14" fill="#c8202f"/><rect y="5.5" width="23" height="3" fill="#c8202f"/></svg>
    <span>English</span>
  </div>

  <nav class="abs nav">
    <div class="abs nav-tab"></div>
    <a class="active" style="left:486px;">HOME</a>
    <a style="left:546px;">ABOUT US</a>
    <a style="left:622px;">SERVICES</a>
    <a style="left:695px;">TESTIMONIALS</a>
    <a style="left:792px;">CONTACT</a>
  </nav>
</header>

<div class="abs bar" style="top:146px;"></div>
<div class="abs hero" role="img" aria-label="Rope access technicians working on the curved glass facade of a tall building, seen from below"></div>
<div class="abs bar" style="top:537px;"></div>

<div class="abs caption">
  <h1>LOREM IPSUM DOLOR SIT AMET, ELIT</h1>
  <p>Cum sociis natoque penatibus et magnis dis parturient montes, nascetur ridiculus mus. In iaculis facilisis massa. Etiam eu urna. Sed porta.Cum sociis natoque penatibus et magnis dis parturient montes, nascetur ridiculus mus. In iaculis facilisis massa. Etiam eu urna. Sed porta.</p>
</div>
<div class="abs arrow" style="left:848px;"><svg viewBox="0 0 33 32"><path d="M19 9 L13 16 L19 23" fill="none" stroke="#6b6d70" stroke-width="1.3"/></svg></div>
<div class="abs arrow" style="left:888px;"><svg viewBox="0 0 33 32"><path d="M14 9 L20 16 L14 23" fill="none" stroke="#6b6d70" stroke-width="1.3"/></svg></div>

<main>
  <h2 class="abs section-title" style="left:100px; top:553px;">Our Services</h2>

  <div class="abs service" style="left:86px;"><div class="service-photo" role="img" aria-label="Rope access worker on a building facade" style="background:linear-gradient(160deg,#dfe6ee,#9fb3c9 55%,#5e6f86);"></div></div>
  <div class="abs service" style="left:246px;"><div class="service-photo" role="img" aria-label="Two climbers working at height beside a blue column" style="background:linear-gradient(160deg,#e2e5ea,#8aa0bd 50%,#2c5aa0);"></div></div>
  <div class="abs service" style="left:398px;"><div class="service-photo" role="img" aria-label="Confined industrial space with a ladder and steel beams" style="background:linear-gradient(170deg,#3b4450,#4f6a66 50%,#1f2428);"></div></div>
  <div class="abs service" style="left:559px;"><div class="service-photo" role="img" aria-label="Worker on a rooftop overlooking a city" style="background:linear-gradient(180deg,#8e9aa3,#b8a78a 55%,#c7a97e);"></div></div>
  <div class="abs service" style="left:716px;"><div class="service-photo" role="img" aria-label="Silhouette of a window cleaner on a glass wall" style="background:linear-gradient(160deg,#e9f1f8,#7fb3dd 50%,#1f5f9c);"></div></div>

  <span class="service-name" style="left:116px; top:753px;">Rope Access</span>
  <span class="service-name" style="left:270px; top:745px;">Work at Height &amp;<br>Difficult Access<br>services</span>
  <span class="service-name" style="left:429px; top:745px;">Water Leak<br>into Buildings</span>
  <span class="service-name" style="left:582px; top:745px;">External Renovation<br>of Buildings</span>
  <span class="service-name" style="left:745px; top:745px;">Windows Cleaning</span>

  <section class="abs welcome">
    <h2 class="block-title">WELCOME TO ORVIK LINES</h2>
    <p class="lead">Mauris vel lacus vitae felis vestibulum volutpat. Etiam est nunc, venisl.</p>
    <p class="body">Sed ut perspiciatis unde omnis iste natus error sit voluptatem accusantium doloremque laudantium, totam rem aperiam, eaque ipsa quae ab illo inventore veritatis et quasi architecto beatae vitae dicta sunt explicabo. Nemo enim ipsam voluptatem quia voluptas sit aspernatur aut odit aut fugit, sed quia consequuntur magni dolores eos qui ratione voluptatem sequi nesciunt. Neque porro quisquam est, qui dolorem ipsum quia dolor sit amet. Nemo enim ipsam voluptatem quia voluptas sit aspernatur aut odit aut fugit, sed quia consequuntur magni dolores eos qui ratione voluptatem sequi nesciunt. Neque porro quisquam est, qui dolorem ipsum quia dolor sit amet.</p>
  </section>
  <div class="abs btn" style="left:495px; top:990px; width:63px;">Read More</div>

  <section class="abs news"><h2 class="block-title">NEWS</h2></section>
  <div class="news-item" style="top:872px;">
    <div class="news-date">Apr 17</div>
    <p class="news-text">Sed ut perspiciatis unde omnis iste natus error sit voluptatem accusantium doloremque rem aperiam, eaque ipsa quae ab illo inven.</p>
  </div>
  <div class="news-item" style="top:936px;">
    <div class="news-date">Apr 17</div>
    <p class="news-text">Sed ut perspiciatis unde omnis iste natus error sit voluptatem accusantium doloremque rem aperiam, eaque ipsa quae ab illo inven.</p>
  </div>
  <div class="abs btn" style="left:778px; top:990px; width:64px;">Read More</div>
</main>

<footer class="abs footer">
  <h3>Newsletter</h3>
  <div class="email">Your Email Id</div>
  <div class="subscribe">Subscribe</div>

  <span class="social" style="left:668px; background:#3b5a99;"></span>
  <span class="social" style="left:698px; background:#4bb8e6;"></span>
  <span class="social" style="left:728px; background:#2f3033;"></span>
  <span class="social" style="left:759px; background:#e7962a;"></span>
  <span class="social" style="left:789px; background:#d8334a; border-radius:50%;"></span>
  <span class="social" style="left:819px; background:#6f9cc0;"></span>

  <div class="links">Privacy<span>|</span>Terms of Use<span>|</span>FAQ<span>|</span>Contact Us</div>
  <div class="copyright">© 2013 Orvik Lines, All rights reserved</div>
</footer>

</body>
</html>
```